Creative Fitness Studio Feature Wall

Two feature walls within functional fitness studio, they need to be on brand and have a WOW factor.
Designed to inspire and motivate people to live a fit and healthy lifestyle whilst working out and bringing life to the studio, as an uplifting and inviting environment.

Please see current walls and also visit website www.velta4.com.au for inspiration.
Updates

Target Market(s)

health and fitness, healthy lifestyle

Industry/Entity Type

Fitness

Font styles to use
Other font styles liked:
• gothic

Colors

Designer to choose colors to be used in the design.

Requirements
Must have
• inspiration from website www.velta4.com.au ........... brand consistency
Nice to have
• WOW factor......... walk into the gym and it draws your attention.
Should not have
• Overly muscly people (bodybuilders)

```html
<!DOCTYPE html>
<html lang="en">
<head>
<meta charset="utf-8">
<title>Velta4 Fitness – Studio Feature Wall</title>
<link rel="stylesheet" href="https://fonts.googleapis.com/css2?family=Roboto:wght@500;700&display=swap">
<style>
  :root {
    --wall: #efedea;
    --ink: #1b1b1b;
    --blue-a: #2a7fd0;
    --blue-b: #45b6ea;
    --magenta-a: #c81f8e;
    --magenta-b: #7d2f93;
    --red-a: #e2503f;
    --red-b: #c8322f;
    --green-a: #6fc63f;
    --green-b: #2f9a54;
    --white: #ffffff;
    --skin: #d9a78a;
    --kit-blue: #3d86c4;
  }
  * { margin: 0; padding: 0; box-sizing: border-box; }
  html, body { width: 1200px; height: 900px; overflow: hidden; background: var(--wall); }
  .feature-wall {
    position: relative;
    width: 1200px;
    height: 900px;
    background: var(--wall);
    font-family: "Roboto", Arial, sans-serif;
    overflow: hidden;
  }
  .wall-art { position: absolute; inset: 0; }
  .brand {
    position: absolute;
    left: 48px;
    top: 118px;
    color: var(--ink);
    font-weight: 700;
    line-height: 1;
  }
  .brand-name { display: block; font-size: 92px; letter-spacing: -2px; }
  .brand-tag { display: block; font-size: 30px; letter-spacing: 6px; margin: 6px 0 0 64px; }
  .quote {
    position: absolute;
    color: var(--white);
    text-align: center;
    font-weight: 500;
    line-height: 1.05;
    text-transform: uppercase;
  }
  .quote strong { font-weight: 700; display: block; }
  .quote-life { left: 440px; top: 165px; width: 320px; }
  .quote-life .small { font-size: 34px; }
  .quote-life strong { font-size: 64px; }
  .quote-challenge { left: 675px; top: 395px; width: 410px; }
  .quote-challenge .small { font-size: 34px; }
  .quote-challenge strong { font-size: 68px; }
</style>
</head>
<body>
<main class="feature-wall">
  <svg class="wall-art" width="1200" height="900" viewBox="0 0 1200 900">
    <defs>
      <linearGradient id="blue-tile" x1="0" y1="1" x2="1" y2="0">
        <stop offset="0" stop-color="var(--blue-a)"/>
        <stop offset="1" stop-color="var(--blue-b)"/>
      </linearGradient>
      <linearGradient id="magenta-tile" x1="0" y1="0" x2="1" y2="1">
        <stop offset="0" stop-color="var(--magenta-a)"/>
        <stop offset="1" stop-color="var(--magenta-b)"/>
      </linearGradient>
      <linearGradient id="red-tile" x1="0" y1="0" x2="1" y2="1">
        <stop offset="0" stop-color="var(--red-a)"/>
        <stop offset="1" stop-color="var(--red-b)"/>
      </linearGradient>
      <linearGradient id="green-tile" x1="0" y1="0" x2="1" y2="1">
        <stop offset="0" stop-color="var(--green-a)"/>
        <stop offset="1" stop-color="var(--green-b)"/>
      </linearGradient>
      <linearGradient id="athlete-tone" x1="0" y1="0" x2="0" y2="1">
        <stop offset="0" stop-color="var(--skin)" stop-opacity="0.55"/>
        <stop offset="1" stop-color="var(--kit-blue)" stop-opacity="0.45"/>
      </linearGradient>
    </defs>

    <polygon class="tile tile-class" role="img" aria-label="Group fitness class photo tinted red"
             points="865,-60 1070,145 865,350 660,145" fill="url(#red-tile)"/>
    <polygon class="tile tile-yoga" role="img" aria-label="Yoga and stretching class photo tinted green"
             points="1200,70 1200,590 940,330" fill="url(#green-tile)"/>
    <polygon class="tile tile-life" role="img" aria-label="Smiling woman photo tinted blue"
             points="600,95 825,320 600,545 375,320" fill="url(#blue-tile)"/>
    <polygon class="tile tile-challenge" role="img" aria-label="Woman training photo tinted magenta"
             points="880,285 1155,560 880,835 605,560" fill="url(#magenta-tile)"/>

    <g class="athletes" fill="url(#athlete-tone)">
      <rect role="img" aria-label="Woman in a back-bend stretch" x="150" y="330" width="230" height="310" rx="110"/>
      <rect role="img" aria-label="Man stretching arms overhead" x="20" y="500" width="240" height="400" rx="110"/>
      <rect role="img" aria-label="Woman in a side-bend stretch" x="180" y="640" width="280" height="260" rx="110"/>
      <rect role="img" aria-label="Male sprinter mid-stride" x="440" y="620" width="370" height="280" rx="120"/>
      <rect role="img" aria-label="Older man doing a push-up" x="680" y="690" width="480" height="210" rx="100"/>
    </g>
  </svg>

  <div class="brand">
    <span class="brand-name">VELTA4</span>
    <span class="brand-tag">FITNESS</span>
  </div>

  <p class="quote quote-life">
    <span class="small">One</span>
    <strong>Life</strong>
    <span class="small">One</span>
    <strong>Chance</strong>
  </p>

  <p class="quote quote-challenge">
    <span class="small">If it<br>doesn't</span>
    <strong>Challenge</strong>
    <span class="small">you, it doesnt</span>
    <strong>Change</strong>
    <span class="small">you</span>
  </p>
</main>
</body>
</html>
```